Coral Voyage Mate - A Travel Services Website

Islestay Cottage Rentals is a company that provides travels services to home owners and travellers to Barbados. Coral Voyage Mate is a particular brand targeting travelling guests with specific set of travel services. The brand slogan is:

'Getting you the best for less'

The travel services will include:

- Coral Voyage Mate Perk Pass
- Car Hire Quote Service
- Mobile Phone Sim Cards
- Prepaid Debit Cards
- Airport Hotel Booking
- Airport Lounge Booking
- Airport Parking

There will also be a travel planner function for guests.

The main puropse of the site is as follows:

1. Registration for the Coral Voyage Mate Perk Pass

2. Creation of user account which the guest will frequently return to check for updates

3. Purchase of ancillary travel products and services

4. To use the Travel Planner

5. To gather data on holiday home owners in Barbados

A site map can be seen at the following link:

http://plotgrid-example.com/charts/viewChart/4kqzvb8ynhpwe2ufa6rj0xmc51tlsg9odiq3ye70bnc8hva2wk

Webpage templates (2 required)

The first will be form control heavy (text boxes, checkboxes ect). It will need failure and success messages / indicators etc.

The second will be a general content area with a secondary navigation area (i.e for sub sections of the current section). This will house text / headings and images.

Both will require header, primary navigation, content and footer areas.

N.B. Please not that I am not technical and the above webtemplate narrative has been supplied by my web developer/programmer. If you have any questions, please ask me any questions and I will get an answer from him.

Target Market(s)

My customers tend to be:

Sex: Female
Age: 24-55
Location: UK, USA, Canada
Social Class: A,B,C1
Income: Medium income bracket

They are possibly visiting Barbados for the first and only time. It is an expensive destination and is accessible to people with a medium to high income. They still desire 'value for money'. Therefore the sight must give guests confidence that Coral Voyage Mate is 'their friend', is seeking to offer the best value deals for their vacation/holiday.

Industry/Entity Type

Travel

Requirements
Must have
• The site templates must be professional, aspirational, trustworthy, reassuring, clean, innovative, fun. When people visit the site they should be excited about the savings that they can make and want to return as there is a perceived benefit for them. It must look expensive and professional in its projected image.
Nice to have
• Smooth currved lines, seperated boxed areas for content, as simple and uncluttered layout and it must be simple to read!
Should not have
• It should not be cartoonly, despite my attached logo and must not look cheap.

```html
<!DOCTYPE html>
<html lang="en">
<head>
<meta charset="utf-8">
<title>Coral Voyage Mate – Account Settings</title>
<link href="https://fonts.googleapis.com/css2?family=Open+Sans:ital,wght@0,400;0,600;0,700;1,700&family=PT+Sans:wght@400;700&display=swap" rel="stylesheet">
<style>
:root{
  --sky-top:#1f8fe0;
  --sky-mid:#6cc0f0;
  --sea:#5fd0d8;
  --sand:#efe9dd;
  --sand-deep:#e6ded0;
  --nav-red:#d5121b;
  --nav-red-dark:#a70c12;
  --brand-red:#d5121b;
  --title-blue:#1ba8e0;
  --label:#505050;
  --heading:#555;
  --panel:#fafafa;
  --box-border:#e4e4e4;
  --field-border:#d6d6d6;
  --orange:#f7a81b;
  --orange-dark:#e98f0a;
  --accent-orange:#f07d12;
  --white:#fff;
}
*{box-sizing:border-box;margin:0;padding:0}
html,body{width:1040px;height:1200px;overflow:hidden}
body{font-family:Arial,Helvetica,sans-serif;color:var(--label);
  background:linear-gradient(180deg,var(--sky-top) 0,var(--sky-mid) 200px,#a8def5 300px,var(--sea) 360px,#cfe9e4 420px,var(--sand) 520px,var(--sand-deep) 1100px);}
.page{position:relative;width:1040px;height:1200px}
.abs{position:absolute}

/* header */
.brand{left:88px;top:30px;display:flex;align-items:center;gap:10px}
.brand-mark{width:34px;height:34px;border-radius:50%;background:var(--brand-red)}
.brand-name{font-family:"Open Sans",sans-serif;font-weight:700;font-size:30px;color:var(--brand-red);line-height:1}
.login{left:486px;top:82px;display:flex;gap:7px;align-items:center}
.login .field{width:112px;height:24px;border-radius:4px;background:#fff;border:1px solid #cfe3f2;font-size:12px;color:#555;padding:4px 8px;display:flex;align-items:center;gap:5px}
.login .btn{width:50px;height:24px;border-radius:4px;background:linear-gradient(#4fc6f2,#1aa4de);color:#fff;font-size:12px;display:flex;align-items:center;justify-content:center;border:1px solid #9ddcf5}
.login .links{font-size:11px;color:#fff;line-height:13px;margin-left:2px}

/* nav */
.nav{left:89px;top:116px;width:868px;height:40px;border-radius:12px 12px 0 0;background:linear-gradient(var(--nav-red),var(--nav-red-dark));display:flex;align-items:center;padding-left:14px}
.nav a{font-family:"PT Sans",sans-serif;color:#fff;font-size:14.5px;text-decoration:none;margin-right:14.5px;white-space:nowrap}

/* hero */
.hero{left:89px;top:156px;width:868px;height:228px;border-radius:0 0 12px 12px;overflow:hidden;box-shadow:0 2px 4px rgba(0,0,0,.25)}
.hero-scene{position:absolute;inset:0;background:linear-gradient(180deg,#2e8fd8 0,#8cc9ef 35%,#5fc8d0 52%,#e8e3d6 62%,#f2eee6 100%)}
.hero-copy{position:absolute;left:28px;top:52px;color:#fff;text-shadow:0 1px 2px rgba(0,0,0,.45)}
.hero-title{font-family:"Open Sans",sans-serif;font-style:italic;font-weight:700;font-size:32px;line-height:38px;letter-spacing:-.6px;white-space:nowrap}
.hero-sub{font-family:"PT Sans",sans-serif;font-weight:700;font-size:17px;margin-top:3px}
.hero-text{font-size:14px;font-weight:700;line-height:18px;margin-top:2px;width:460px}
.apply{position:absolute;left:31px;top:164px;width:102px;height:25px;border-radius:5px;background:linear-gradient(#fdc13b,var(--orange-dark));color:#fff;font-family:"PT Sans",sans-serif;font-weight:700;font-size:14px;display:flex;align-items:center;justify-content:center;text-shadow:0 1px 1px rgba(0,0,0,.3)}
.hero-card{position:absolute;left:495px;top:36px;width:280px;height:170px;border-radius:10px;background:linear-gradient(135deg,#bfe6f7,#7fc8e8 50%,#e9f4f8);box-shadow:0 2px 6px rgba(0,0,0,.35)}
.pager{position:absolute;left:781px;top:198px;display:flex;gap:4px}
.pager span{width:15px;height:15px;border-radius:3px;background:#fff;color:var(--nav-red);font-size:10px;display:flex;align-items:center;justify-content:center}
.pager span.on{background:var(--nav-red);color:#fff}

/* footer band sits behind the panel */
.footer-band{left:0;top:1110px;width:1040px;height:90px;background:linear-gradient(var(--orange),#f5a414);z-index:0}

/* panel */
.panel{left:90px;top:411px;width:865px;height:738px;border-radius:10px;background:var(--panel);box-shadow:0 1px 4px rgba(0,0,0,.25);z-index:2}
.panel-head{position:absolute;left:0;top:0;width:100%;height:44px;border-radius:10px 10px 0 0;background:#fff;border-bottom:1px solid #e8e8e8}
.flower{position:absolute;left:14px;top:9px;width:36px;height:36px;border-radius:50%;background:radial-gradient(#f25a4a,#c8141b)}
.shells{position:absolute;left:718px;top:-12px;width:150px;height:70px;border-radius:35px;background:radial-gradient(ellipse at 40% 45%,rgba(233,176,125,.9),rgba(214,143,75,.55) 60%,rgba(214,143,75,0) 75%)}
.panel-title{position:absolute;left:61px;top:13px;font-size:17px;font-weight:700;color:var(--title-blue)}
.section-title{position:absolute;left:20px;font-size:14px;font-weight:700;color:var(--heading);display:flex;align-items:center;gap:6px}
.section-title i{width:9px;height:9px;background:var(--accent-orange);display:block}
.box{position:absolute;left:18px;width:819px;border:1px solid var(--box-border);border-radius:6px;background:#fff}
.row{position:absolute;left:0;width:100%;height:24px}
.row label{position:absolute;left:23px;top:4px;font-size:14px;color:var(--label)}
.input{position:absolute;top:0;width:188px;height:24px;border:1px solid var(--field-border);border-radius:5px;background:linear-gradient(#f1f1f1,#fff 40%);box-shadow:inset 0 1px 2px rgba(0,0,0,.1)}
.select{position:absolute;top:0;height:24px;border:1px solid var(--field-border);border-radius:5px;background:#f7f7f7;font-size:13px;color:#999;padding:4px 9px}
.select svg{position:absolute;right:5px;top:5px}
.check{position:absolute;left:22px;display:flex;align-items:center;gap:8px;font-size:14px;color:var(--label)}
.check i{width:12px;height:12px;border:1px solid #999;background:linear-gradient(#fff,#ddd);display:block}
.btn-red{position:absolute;top:700px;width:94px;height:26px;border-radius:5px;background:linear-gradient(#e8323a,#a80d12);color:#fff;font-size:14px;font-weight:700;display:flex;align-items:center;justify-content:center;box-shadow:0 1px 2px rgba(0,0,0,.35)}

/* footer text */
.copyright{left:93px;top:1166px;font-size:12px;color:#fff;z-index:3}
.social{top:1162px;height:23px;border-radius:3px;font-size:11.5px;font-weight:700;display:flex;align-items:center;gap:5px;padding-left:6px;z-index:3;white-space:nowrap}
.social i{width:10px;height:10px;display:block}
.social.flock{left:782px;width:80px;background:linear-gradient(#e4f6fc,#a9dcef);color:#3d7fa3}
.social.flock i{background:#3d9fd0}
.social.wall{left:869px;width:84px;background:linear-gradient(#5b79b4,#3b5592);color:#fff}
.social.wall i{background:#fff}
</style>
</head>
<body>
<div class="page">

  <header>
    <div class="abs brand"><span class="brand-mark"></span><span class="brand-name">Coral Voyage Mate</span></div>
    <form class="abs login">
      <div class="field"><svg width="9" height="10" viewBox="0 0 9 10"><circle cx="4.5" cy="3" r="2.5" fill="#999"/><path d="M0 10a4.5 4 0 0 1 9 0z" fill="#999"/></svg>username</div>
      <div class="field">password</div>
      <div class="btn">Login</div>
      <div class="links">Forgot Password?<br>Register New</div>
    </form>
    <nav class="abs nav">
      <a>Airport Parking</a><a>Airport Hotel</a><a>Airport Lounge</a><a>Car Hire</a><a>Attractions</a><a>Travel Money</a><a>Mobile Sim Cards</a><a>Privilege Card</a>
    </nav>
    <section class="abs hero">
      <div class="hero-scene" role="img" aria-label="Sunny beach with thatched parasol, loungers, sea and palm tree"></div>
      <div class="hero-copy">
        <div class="hero-title">Getting you the best for less</div>
        <div class="hero-sub">Coral Voyage Mate Perk Pass</div>
        <div class="hero-text">Lorem ipsum dolor sit amet, consectetur adipiscing elit. Nullam metus nisi, sagittis semper cursus id, sollicitudin non justo.</div>
      </div>
      <div class="apply">Apply Now!</div>
      <div class="hero-card" role="img" aria-label="Perk pass cards from Islestay Cottage Rentals with a palm beach picture, issued to Helen Marsh"></div>
      <div class="pager"><span class="on">1</span><span>2</span><span>3</span><span>4</span></div>
    </section>
  </header>

  <div class="abs footer-band"></div>

  <main class="abs panel">
    <div class="panel-head">
      <div class="flower" role="img" aria-label="Red hibiscus flower"></div>
      <div class="panel-title">Account Settings</div>
      <div class="shells" role="img" aria-label="Sea shells and starfish"></div>
    </div>

    <div class="section-title" style="top:68px"><i></i>Your Details</div>
    <div class="box" style="top:88px;height:127px">
      <div class="row" style="top:19px"><label>Email Address</label><span class="input" style="left:201px"></span></div>
      <div class="row" style="top:52px"><label>Password</label><span class="input" style="left:201px"></span></div>
      <div class="row" style="top:84px"><label>Confirm Password</label><span class="input" style="left:201px"></span></div>
    </div>

    <div class="section-title" style="top:236px"><i></i>Personal Details</div>
    <div class="box" style="top:256px;height:302px">
      <div class="row" style="top:19px"><label>First Name</label><span class="input" style="left:203px"></span></div>
      <div class="row" style="top:52px"><label>Last Name</label><span class="input" style="left:203px"></span></div>
      <div class="row" style="top:85px"><label>House Number / Street</label><span class="input" style="left:204px"></span></div>
      <div class="row" style="top:119px"><label>Line 2</label><span class="input" style="left:205px"></span></div>
      <div class="row" style="top:152px"><label>Town</label><span class="input" style="left:205px"></span></div>
      <div class="row" style="top:185px"><label>Country</label><span class="select" style="left:205px;width:188px">Select<svg width="14" height="14"><rect x=".5" y=".5" width="13" height="13" fill="#eee" stroke="#555"/><path d="M4 5h6l-3 4z" fill="#222"/></svg></span></div>
      <div class="row" style="top:219px"><label>Phone</label><span class="input" style="left:205px"></span></div>
      <div class="row" style="top:252px"><label>Departure Date</label>
        <span class="select" style="left:205px;width:68px">Jan<svg width="14" height="14"><rect x=".5" y=".5" width="13" height="13" fill="#eee" stroke="#555"/><path d="M4 5h6l-3 4z" fill="#222"/></svg></span>
        <span class="select" style="left:281px;width:68px">01<svg width="14" height="14"><rect x=".5" y=".5" width="13" height="13" fill="#eee" stroke="#555"/><path d="M4 5h6l-3 4z" fill="#222"/></svg></span>
        <span class="select" style="left:356px;width:68px">2010<svg width="14" height="14"><rect x=".5" y=".5" width="13" height="13" fill="#eee" stroke="#555"/><path d="M4 5h6l-3 4z" fill="#222"/></svg></span>
      </div>
    </div>

    <div class="section-title" style="top:579px"><i></i>Account Options</div>
    <div class="box" style="top:600px;height:81px">
      <div class="check" style="top:21px"><i></i>Receive weekly email updated</div>
      <div class="check" style="top:49px"><i></i>Receive Seleced offers</div>
    </div>

    <div class="btn-red" style="left:21px">Submit</div>
    <div class="btn-red" style="left:122px">Reset</div>
  </main>

  <footer>
    <div class="abs copyright">Copyright © 2010 Coral Voyage Mate. All rights reserved.</div>
    <div class="abs social flock"><i></i>Flockpost</div>
    <div class="abs social wall"><i></i>Friendwall</div>
  </footer>
</div>
</body>
</html>
```